Anzeigengestaltung für Steuerberater
Zielgruppe
aufgrund Unsimmitgkeiten mit pixelwerkhof.de, bitte ich Sie, diesen Event hier zu ignorieren.
Aufgabenstellung

```html
<!DOCTYPE html>
<html lang="de">
<head>
<meta charset="utf-8">
<title>Gutschein – Vitamin C für Ihre Steuererklärung</title>
<link href="https://fonts.googleapis.com/css2?family=Barlow+Condensed:wght@400;600;700&display=swap" rel="stylesheet">
<style>
  :root {
    --bg: #f0f2f1;
    --frame: #96979b;
    --paper: #ffffff;
    --ink: #1d1d1b;
    --teal: #6db4c1;
    --band-light: #cdeef2;
    --band-dark: #8ecdd6;
    --stripe-dark: #7fc0cb;
    --stripe-light: #c6e9ee;
    --badge: #58595b;
  }
  html, body {
    margin: 0;
    padding: 0;
    width: 1195px;
    height: 1200px;
    overflow: hidden;
    background: var(--bg);
  }
  .voucher {
    display: block;
    width: 1195px;
    height: 1200px;
    font-family: "Barlow Condensed", "Arial Narrow", sans-serif;
  }
  .headline { font-weight: 600; fill: var(--ink); }
  .copy { font-weight: 600; fill: var(--ink); }
  .amount { font-weight: 600; fill: var(--teal); }
  .cta-label { font-weight: 400; fill: var(--paper); }
  .decline { font-weight: 400; fill: var(--ink); text-decoration: underline; }
  .badge-label {
    font-weight: 700;
    fill: var(--paper);
    stroke: var(--ink);
    stroke-width: 2.5;
    paint-order: stroke fill;
  }
</style>
</head>
<body>
<svg class="voucher" viewBox="0 0 1195 1200" xmlns="http://www.w3.org/2000/svg">
  <defs>
    <linearGradient id="band-fill" x1="0" y1="0" x2="1" y2="0">
      <stop offset="0" stop-color="var(--band-light)"/>
      <stop offset="0.5" stop-color="var(--band-light)"/>
      <stop offset="1" stop-color="var(--band-dark)"/>
    </linearGradient>
    <linearGradient id="stripe-fill" x1="0" y1="0" x2="1" y2="0">
      <stop offset="0" stop-color="var(--stripe-dark)"/>
      <stop offset="1" stop-color="var(--stripe-light)"/>
    </linearGradient>
    <clipPath id="card-clip">
      <rect x="356" y="178" width="481" height="794" rx="56"/>
    </clipPath>
    <filter id="card-shadow" x="-20%" y="-20%" width="150%" height="150%">
      <feDropShadow dx="18" dy="22" stdDeviation="16" flood-color="#000" flood-opacity="0.18"/>
    </filter>
  </defs>

  <!-- Card -->
  <g class="card">
    <rect class="card-frame" x="356" y="178" width="481" height="794" rx="56" fill="var(--frame)" filter="url(#card-shadow)"/>
    <rect class="card-paper" x="386" y="208" width="421" height="734" rx="32" fill="var(--paper)"/>

    <g class="card-band" clip-path="url(#card-clip)">
      <path d="M356,373 Q600,270 837,225 L837,491 Q600,482 356,499 Z" fill="url(#band-fill)"/>
      <path d="M356,497 Q600,478 837,487 L837,513 Q600,494 356,509 Z" fill="url(#stripe-fill)"/>
    </g>
  </g>

  <!-- Badge -->
  <g class="badge" transform="translate(409,220)">
    <polygon fill="var(--badge)" points="112,0 96.1,19.1 103.5,42.9 81.4,54.5 79.2,79.2 54.5,81.4 42.9,103.5 19.1,96.1 0,112 -19.1,96.1 -42.9,103.5 -54.5,81.4 -79.2,79.2 -81.4,54.5 -103.5,42.9 -96.1,19.1 -112,0 -96.1,-19.1 -103.5,-42.9 -81.4,-54.5 -79.2,-79.2 -54.5,-81.4 -42.9,-103.5 -19.1,-96.1 0,-112 19.1,-96.1 42.9,-103.5 54.5,-81.4 79.2,-79.2 81.4,-54.5 103.5,-42.9 96.1,-19.1"/>
    <text class="badge-label" x="0" y="20" font-size="58" text-anchor="middle" textLength="186" lengthAdjust="spacingAndGlyphs">GUTSCHEIN</text>
  </g>

  <!-- Headline -->
  <text class="headline" x="597" y="384" font-size="60" text-anchor="middle" textLength="175" lengthAdjust="spacingAndGlyphs">Vitamin C</text>
  <text class="headline" x="597" y="424" font-size="38" text-anchor="middle" textLength="325" lengthAdjust="spacingAndGlyphs">für Ihre Steuererklärung –</text>
  <text class="headline" x="597" y="464" font-size="38" text-anchor="middle" textLength="309" lengthAdjust="spacingAndGlyphs">Einfach und erfrischend!</text>

  <!-- Offer -->
  <text class="copy" x="597" y="548" font-size="38" text-anchor="middle" textLength="245" lengthAdjust="spacingAndGlyphs">Profitieren Sie jetzt</text>
  <text class="copy" x="597" y="585" font-size="38" text-anchor="middle" textLength="125" lengthAdjust="spacingAndGlyphs">von Ihrem</text>
  <text class="amount" x="597" y="675" font-size="104" text-anchor="middle" textLength="130" lengthAdjust="spacingAndGlyphs">30€</text>
  <text class="copy" x="597" y="722" font-size="38" text-anchor="middle" textLength="285" lengthAdjust="spacingAndGlyphs">Neukunden-Gutschein.</text>

  <!-- Actions -->
  <g class="cta">
    <rect x="447" y="776" width="299" height="74" rx="37" fill="var(--teal)"/>
    <text class="cta-label" x="597" y="827" font-size="38" text-anchor="middle" textLength="115" lengthAdjust="spacingAndGlyphs">EINLÖSEN</text>
  </g>
  <text class="decline" x="597" y="878" font-size="19" text-anchor="middle" textLength="83" lengthAdjust="spacingAndGlyphs">NEIN, DANKE.</text>
</svg>
</body>
</html>
```